Redesign cement bags for leading cement producer in south east asia

We are from Larkfield cement and would like to redesign our bag to relaunch the product line. Our bags are made of high quality PP woven sack. We are one of the leading cement producers and we want our bags to have a Larkfield classy look on each visible side when it is loading in a truck or stacking on a pallet.

Thank you for interesting in this project. Good luck.

Project Deadline Extended Reason: Hi all, I have received requests to extend the deadline. Some of the work requires revising and some of them are still on process. To be fair, I also raise my budget to compensate the time. Thanks all for your participation. Added Sunday, July 10, 2016

Target Market(s)

Construction

Industry/Entity Type

Cement

Requirements
Must have
• You will have to design two bags for two cement grades. 52.5 is of higher grade and 42.5 is of lower grade. Both are similar in design but a distinctive colours to differentiate the two at once. Please look at Reference picture 2 for ideas.
Nice to have
• You do not have to change the original logo but the Larkfield cement word font changes are required. There are no restrictions to colours and font but please refrain from using feminine colours. Instructions on rear side of the bags are now included in the scope. Please create new layout and design new user friendly symbols.
Should not have
• Since cement is a dusty product, you need avoid some colours like black as background. The dust need to be less obvious to attract attention. Our previous base colour are shown in below.
• We want a fresh look on our bag, please do not just copy our old design and make small changes. I have attached our competitors' design, please refrain from using their design as well.
• It is recommend to do some research on cement bag sector.

```html
<!DOCTYPE html>
<html lang="en">
<head>
<meta charset="utf-8">
<title>Larkfield Portland Cement – Bag Designs</title>
<link href="https://fonts.googleapis.com/css2?family=Archivo+Black&family=Archivo:wght@700;800&display=swap" rel="stylesheet">
<style>
  :root {
    --backdrop: #b4b4b4;
    --sack: #f4f4f4;
    --sack-shade: #e2e2e2;
    --white: #ffffff;
    --grade-high: #d51a22;
    --grade-high-dark: #b9141b;
    --grade-standard: #1d5aa8;
    --grade-standard-dark: #174a8c;
  }
  * { margin: 0; padding: 0; box-sizing: border-box; }
  html, body { width: 1200px; height: 1198px; overflow: hidden; }
  body {
    background: var(--backdrop);
    font-family: "Archivo Black", "Archivo", sans-serif;
    position: relative;
  }
  .bag {
    position: absolute;
    top: 226px;
    width: 480px;
    height: 870px;
    border-radius: 10px;
    background: linear-gradient(90deg, var(--sack-shade) 0%, var(--sack) 12%, var(--white) 50%, var(--sack) 88%, var(--sack-shade) 100%);
    overflow: hidden;
  }
  .bag--high { left: 100px; --brand: var(--grade-high); --brand-dark: var(--grade-high-dark); }
  .bag--standard { left: 620px; --brand: var(--grade-standard); --brand-dark: var(--grade-standard-dark); }

  .brand-name {
    position: absolute;
    top: 70px; left: 0; right: 0;
    text-align: center;
    font-size: 50px;
    line-height: 1;
    color: var(--brand);
    letter-spacing: 1px;
  }
  .origin {
    position: absolute;
    top: 128px; left: 0; right: 0;
    text-align: center;
    font-family: "Archivo", sans-serif;
    font-weight: 800;
    font-size: 15px;
    color: var(--brand);
    letter-spacing: 0.5px;
  }
  .emblem-area {
    position: absolute;
    top: 190px; left: 115px;
    width: 250px; height: 250px;
  }

  .grade-band {
    position: absolute;
    left: 0; right: 0; top: 470px; bottom: 0;
    background: linear-gradient(180deg, var(--brand) 0%, var(--brand-dark) 100%);
  }
  .weight-panel {
    position: absolute;
    left: 0; bottom: 0;
    width: 205px; height: 240px;
    background: linear-gradient(90deg, var(--sack-shade), var(--white));
    border-top-right-radius: 190px 150px;
  }
  .quality {
    position: absolute;
    top: 26px; left: 0; right: 0;
    text-align: center;
    font-size: 21px;
    color: var(--white);
    letter-spacing: 0.5px;
  }
  .product-name {
    position: absolute;
    top: 56px; left: 0; right: 0;
    text-align: center;
    font-size: 44px;
    line-height: 40px;
    color: var(--white);
  }
  .strength-label {
    position: absolute;
    top: 132px; left: 236px;
    font-family: "Archivo", sans-serif;
    font-weight: 800;
    font-size: 12px;
    line-height: 13px;
    color: var(--white);
  }
  .strength-value {
    position: absolute;
    top: 152px; left: 236px;
    font-size: 96px;
    line-height: 1;
    color: var(--white);
    letter-spacing: -2px;
  }
  .strength-value small { font-size: 46px; letter-spacing: 0; }
  .net-label {
    position: absolute;
    left: 30px; bottom: 150px;
    font-family: "Archivo", sans-serif;
    font-weight: 800;
    font-size: 9px;
    color: var(--brand);
  }
  .net-value {
    position: absolute;
    left: 28px; bottom: 108px;
    font-size: 34px;
    line-height: 1;
    color: var(--brand);
  }
</style>
</head>
<body>

  <section class="bag bag--high" aria-label="Larkfield Portland Cement, strength class 52.5">
    <div class="brand-name">LARKFIELD</div>
    <div class="origin">PRODUCT OF MYANMAR</div>
    <svg class="emblem-area" viewBox="0 0 250 250" role="img" aria-label="Brand emblem area">
      <circle cx="125" cy="125" r="110" fill="var(--brand)" opacity="0.12"/>
    </svg>
    <div class="grade-band">
      <div class="quality">EXPORT QUALITY</div>
      <div class="product-name">PORTLAND<br>CEMENT</div>
      <div class="strength-label">STRENGTH CLASS<br>EN 197-1 (2000)</div>
      <div class="strength-value">52<small>.5</small></div>
      <div class="weight-panel">
        <div class="net-label">NET WEIGHT</div>
        <div class="net-value">50kg</div>
      </div>
    </div>
  </section>

  <section class="bag bag--standard" aria-label="Larkfield Portland Cement, strength class 42.5">
    <div class="brand-name">LARKFIELD</div>
    <div class="origin">PRODUCT OF MYANMAR</div>
    <svg class="emblem-area" viewBox="0 0 250 250" role="img" aria-label="Brand emblem area">
      <circle cx="125" cy="125" r="110" fill="var(--brand)" opacity="0.12"/>
    </svg>
    <div class="grade-band">
      <div class="quality">EXPORT QUALITY</div>
      <div class="product-name">PORTLAND<br>CEMENT</div>
      <div class="strength-label">STRENGTH CLASS<br>EN 197-1 (2000)</div>
      <div class="strength-value">42<small>.5</small></div>
      <div class="weight-panel">
        <div class="net-label">NET WEIGHT</div>
        <div class="net-value">50kg</div>
      </div>
    </div>
  </section>

</body>
</html>
```